Plumbing Company business card design

Create a business card for our plumbing company. Following info needs to be present

Website-prairiepipeworks.com
Email- contact@prairiepipeworks-mail.com
Phone-515-394-2068
Address-4817 NW Cobalt Blvd STE K
Ankeny, Iowa 50347

```html
<!DOCTYPE html>
<html lang="en">
<head>
<meta charset="utf-8">
<title>Prairie Pipeworks – Business Card</title>
<link href="https://fonts.googleapis.com/css2?family=Montserrat:wght@400;500;800&family=Raleway:wght@500;600&display=swap" rel="stylesheet">
<style>
  :root {
    --backdrop: #3a3a3c;
    --paper: #ffffff;
    --brand-blue: #0a4a93;
    --brand-red: #f0171f;
    --ink: #2b2b2b;
    --rule: #9a9a9a;
  }
  * { box-sizing: border-box; margin: 0; padding: 0; }
  html, body { width: 1200px; height: 1200px; overflow: hidden; }
  body {
    background: var(--backdrop);
    font-family: "Montserrat", sans-serif;
    position: relative;
  }
  .card {
    position: absolute;
    left: 110px;
    width: 980px;
    height: 560px;
    border-radius: 34px;
    overflow: hidden;
  }
  .card--front { top: 30px; background: var(--paper); }
  .card--back { top: 610px; background: var(--brand-blue); }

  /* Brand lockup */
  .brand {
    position: absolute;
    display: flex;
    align-items: center;
    gap: 22px;
  }
  .brand__dot {
    border-radius: 50%;
    flex: none;
  }
  .brand__name {
    font-family: "Montserrat", sans-serif;
    font-weight: 800;
    text-transform: uppercase;
    line-height: 1.05;
    letter-spacing: 1px;
  }
  .card--front .brand { left: 90px; top: 120px; }
  .card--front .brand__dot { width: 92px; height: 92px; background: var(--brand-red); }
  .card--front .brand__name { font-size: 44px; color: var(--brand-red); }

  .card--back .brand { left: 50%; top: 50%; transform: translate(-50%, -50%); }
  .card--back .brand__dot { width: 130px; height: 130px; background: var(--brand-red); }
  .card--back .brand__name { font-size: 60px; color: var(--brand-red); }

  /* Divider */
  .divider {
    position: absolute;
    left: 500px;
    top: 300px;
    width: 1px;
    height: 130px;
    background: var(--rule);
  }

  /* Contact list */
  .contact {
    position: absolute;
    left: 540px;
    top: 290px;
    list-style: none;
    display: flex;
    flex-direction: column;
    gap: 12px;
  }
  .contact__item {
    display: flex;
    align-items: flex-start;
    gap: 12px;
    font-size: 17px;
    color: var(--ink);
    line-height: 1.25;
  }
  .contact__icon { width: 20px; height: 20px; flex: none; margin-top: 1px; }

  /* Person */
  .person {
    position: absolute;
    left: 60px;
    top: 382px;
    padding-left: 18px;
    border-left: 6px solid var(--brand-red);
  }
  .person__name {
    font-family: "Raleway", sans-serif;
    font-weight: 600;
    font-size: 38px;
    color: var(--brand-red);
    text-transform: uppercase;
    line-height: 1;
  }
  .person__role {
    font-family: "Raleway", sans-serif;
    font-weight: 500;
    font-size: 20px;
    color: var(--ink);
    text-transform: uppercase;
    margin-top: 2px;
  }

  /* Bottom bands */
  .band { position: absolute; bottom: 0; }
  .band--blue { left: 0; width: 590px; height: 36px; background: var(--brand-blue); }
  .band--red { left: 602px; right: 0; height: 60px; background: var(--brand-red); }
</style>
</head>
<body>

<section class="card card--front" aria-label="Card front">
  <div class="brand">
    <span class="brand__dot"></span>
    <span class="brand__name">Prairie<br>Pipeworks</span>
  </div>

  <div class="divider"></div>

  <ul class="contact">
    <li class="contact__item">
      <svg class="contact__icon" viewBox="0 0 24 24"><path fill="#f0171f" d="M6.6 10.8a15 15 0 0 0 6.6 6.6l2.2-2.2c.3-.3.7-.4 1-.2 1.1.4 2.3.6 3.6.6.6 0 1 .4 1 1V20c0 .6-.4 1-1 1A17 17 0 0 1 3 4c0-.6.4-1 1-1h3.5c.6 0 1 .4 1 1 0 1.3.2 2.5.6 3.6.1.3 0 .7-.2 1z"/></svg>
      <span>515-394-2068</span>
    </li>
    <li class="contact__item">
      <svg class="contact__icon" viewBox="0 0 24 24" fill="none" stroke="#f0171f" stroke-width="2"><circle cx="12" cy="12" r="9"/><path d="M3 12h18M12 3c3 3 3 15 0 18M12 3c-3 3-3 15 0 18"/></svg>
      <span>www.prairiepipeworks.com</span>
    </li>
    <li class="contact__item">
      <svg class="contact__icon" viewBox="0 0 24 24"><rect x="2" y="5" width="20" height="14" rx="1" fill="#f0171f"/><path d="M2 6l10 7 10-7" fill="none" stroke="#fff" stroke-width="1.6"/></svg>
      <span>contact@prairiepipeworks-mail.com</span>
    </li>
    <li class="contact__item">
      <svg class="contact__icon" viewBox="0 0 24 24"><path fill="#f0171f" d="M12 2a7 7 0 0 0-7 7c0 5 7 13 7 13s7-8 7-13a7 7 0 0 0-7-7zm0 9.5A2.5 2.5 0 1 1 12 6.5a2.5 2.5 0 0 1 0 5z"/></svg>
      <span>4817 NW Cobalt Blvd STE K<br>Ankeny, Iowa 50347</span>
    </li>
  </ul>

  <div class="person">
    <p class="person__name">Delaney</p>
    <p class="person__role">Owner</p>
  </div>

  <div class="band band--blue"></div>
  <div class="band band--red"></div>
</section>

<section class="card card--back" aria-label="Card back">
  <div class="brand">
    <span class="brand__dot"></span>
    <span class="brand__name">Prairie<br>Pipeworks</span>
  </div>
</section>

</body>
</html>
```